Marine Collagen Powder Label Re-design

Give me alternative design options for one of my products - Marine Collagen Powder. I need the RAW file as output in Adobe Illustrator format - clearly defined and labelled layers - as a fully editable and properly label each layer in the file.

I want new and fresh ideas for this label. Use metallic colours if required. Make it more attractive.

```html
<!DOCTYPE html>
<html lang="en">
<head>
<meta charset="UTF-8">
<title>Vitalora Marine Collagen Powder – Label Options</title>
<link href="https://fonts.googleapis.com/css2?family=Montserrat:wght@500;600;700;800&family=Inter:wght@400;500;600&display=swap" rel="stylesheet">
<style>
  :root {
    --bg-top: #eeeeee;
    --bg-bottom: #dcdcdc;
    --label-white: #ffffff;
    --ink-dark: #2b2b2b;
    --ink-mid: #4a4a4a;
    --ink-soft: #8a8a8a;
    --silver-a: #8c8c8c;
    --silver-b: #f3f3f3;
    --silver-c: #a3a3a3;
    --copper-a: #b4643c;
    --copper-b: #f2b892;
    --copper-c: #ad6540;
    --rule: #d6d6d6;
  }
  * { box-sizing: border-box; margin: 0; padding: 0; }
  html, body { width: 1200px; height: 661px; overflow: hidden; }
  body {
    position: relative;
    background: linear-gradient(180deg, var(--bg-top), var(--bg-bottom));
    font-family: "Inter", Arial, sans-serif;
    color: var(--ink-dark);
  }
  .label {
    position: absolute;
    top: 140px;
    width: 270px;
    height: 395px;
    background: var(--label-white);
    border-radius: 8px;
    box-shadow: 0 6px 18px rgba(0,0,0,0.08);
    text-align: center;
    padding: 78px 20px 0 0;
  }
  .label--one { left: 65px; }
  .label--two { left: 425px; }
  .label--three { left: 780px; }
  .brand-name {
    display: block;
    font-family: "Montserrat", Arial, sans-serif;
    font-weight: 700;
    font-size: 25px;
    line-height: 30px;
    color: var(--ink-dark);
    letter-spacing: -0.3px;
  }
  .tagline {
    font-size: 8px;
    line-height: 10px;
    color: var(--ink-mid);
    margin-top: 2px;
  }
  .grade {
    font-family: "Montserrat", Arial, sans-serif;
    font-weight: 500;
    font-size: 12px;
    line-height: 14px;
    letter-spacing: 0.5px;
    margin-top: 13px;
    color: var(--ink-mid);
  }
  .product-name {
    font-family: "Montserrat", Arial, sans-serif;
    font-weight: 800;
    font-size: 28px;
    line-height: 28px;
    color: var(--ink-dark);
    margin-top: 3px;
  }
  .band {
    margin: 7px -10px 0 10px;
    height: 36px;
    display: flex;
    flex-direction: column;
    justify-content: center;
    line-height: 1.15;
  }
  .band--silver { background: linear-gradient(90deg, var(--silver-a), var(--silver-b) 50%, var(--silver-c)); }
  .band--copper { background: linear-gradient(90deg, var(--copper-a), var(--copper-b) 50%, var(--copper-c)); }
  .band-title {
    font-family: "Montserrat", Arial, sans-serif;
    font-weight: 800;
    font-size: 12.5px;
    color: var(--ink-dark);
  }
  .band-sub {
    font-family: "Montserrat", Arial, sans-serif;
    font-weight: 600;
    font-size: 9px;
    color: var(--ink-dark);
  }
  .benefits {
    font-size: 12px;
    line-height: 14px;
    color: var(--ink-mid);
    margin-top: 8px;
  }
  .spec-row {
    display: flex;
    justify-content: space-between;
    padding: 0 16px 0 36px;
    margin-top: 16px;
    font-family: "Montserrat", Arial, sans-serif;
    font-weight: 600;
    font-size: 7px;
    line-height: 10px;
    color: var(--ink-mid);
  }
  .spec-bottom {
    display: flex;
    justify-content: space-between;
    align-items: center;
    padding: 0 16px 0 34px;
    margin-top: 5px;
  }
  .quality-pill {
    font-size: 6px;
    font-weight: 600;
    color: #fff;
    padding: 3px 8px;
    border-radius: 8px;
    text-transform: uppercase;
  }
  .quality-pill--silver { background: var(--silver-c); }
  .quality-pill--copper { background: var(--copper-a); }
  .free-from {
    font-size: 6px;
    color: var(--ink-soft);
  }
  .side-panel {
    position: absolute;
    right: 4px;
    top: 82px;
    width: 20px;
    text-align: left;
    font-size: 4px;
    line-height: 1.5;
    color: var(--ink-soft);
  }
  .side-panel p { margin-bottom: 14px; }
  .side-panel .box {
    border: 0.6px solid var(--rule);
    padding: 2px 1px;
    margin-bottom: 14px;
  }
</style>
</head>
<body>
<main class="label-set">

  <section class="label label--one">
    <span class="brand-name">vitalora</span>
    <p class="tagline">Daily Care. Pure Balance.</p>
    <p class="grade">PREMIUM</p>
    <h1 class="product-name">MARINE<br>COLLAGEN<br>POWDER</h1>
    <div class="band band--silver">
      <span class="band-title">PURE CORE</span>
      <span class="band-sub">For Skin, Hair, Nails &amp; Joints</span>
    </div>
    <p class="benefits">For Skin, Hair, Nails &amp; Joints</p>
    <div class="spec-row"><span>FOOD SUPPLEMENT</span><span>300g POWDER</span><span>30 SERVINGS</span></div>
    <div class="spec-bottom"><span class="quality-pill quality-pill--silver">High Quality &amp; Naturally Sourced</span><span class="free-from">Gluten Free</span></div>
    <div class="side-panel">
      <p>Directions</p>
      <div class="box">Mix 1 scoop</div>
      <p>in 200 ml water</p>
      <div class="box">Store cool, dry</div>
    </div>
  </section>

  <section class="label label--two">
    <span class="brand-name">vitalora</span>
    <p class="tagline">Daily Care. Pure Balance.</p>
    <p class="grade">PREMIUM</p>
    <h1 class="product-name">MARINE<br>COLLAGEN<br>POWDER</h1>
    <div class="band band--copper">
      <span class="band-title">PURE CORE</span>
      <span class="band-sub">10,000 MG PER SERVING</span>
    </div>
    <p class="benefits">For Skin, Hair, Nails &amp; Joints</p>
    <div class="spec-row"><span>FOOD SUPPLEMENT</span><span>300g POWDER</span><span>30 SERVINGS</span></div>
    <div class="spec-bottom"><span class="quality-pill quality-pill--copper">High Quality &amp; Naturally Sourced</span><span class="free-from">Gluten Free</span></div>
    <div class="side-panel">
      <p>Directions</p>
      <div class="box">Mix 1 scoop</div>
      <p>in 200 ml water</p>
      <div class="box">Store cool, dry</div>
    </div>
  </section>

  <section class="label label--three">
    <span class="brand-name">vitalora</span>
    <p class="tagline">Daily Care. Pure Balance.</p>
    <p class="grade">PREMIUM</p>
    <h1 class="product-name">MARINE<br>COLLAGEN<br>POWDER</h1>
    <div class="band band--copper">
      <span class="band-title">PURE CORE</span>
      <span class="band-sub">10,000 MG PER SERVING</span>
    </div>
    <p class="benefits">For Skin, Hair, Nails &amp; Joints</p>
    <div class="spec-row"><span>FOOD SUPPLEMENT</span><span>300g POWDER</span><span>30 SERVINGS</span></div>
    <div class="spec-bottom"><span class="quality-pill quality-pill--copper">High Quality &amp; Naturally Sourced</span><span class="free-from">Gluten Free</span></div>
    <div class="side-panel">
      <p>Directions</p>
      <div class="box">Mix 1 scoop</div>
      <p>in 200 ml water</p>
      <div class="box">Store cool, dry</div>
    </div>
  </section>

</main>
</body>
</html>
```